Mobile Interface Design

Take an existing website design and create a Mobile interface that is creative and easy to navigate. Background programming and stuff already accomplished... need a Graphic Designer with Mobile UI expertise. Need it done quickly in 1-2 weeks.
Go to http://demo.fairwaypulse.example. Signup using invitation code "vinodvisitor" - we need the pick players screen designed for a mobile platform. We have some ideas regarding the layout of the screen. I will upload a mockup. We need to stick to current design site as much as possible but also provide a better mobile site experience.
Notes of the attached file:
The header will have Teebeacon logo, Messages icon, Points and menu (lines).
Ignore second bar
Tournament Info will be a scroll down box (mobile expand layer)
Tokens bar will have the tokens from the web page 100/40
The field - will be the players from the website - will show rank, photo, name, token value (20) and a check box - to select. the check box will change the color of the layer. At the top - the filters will be similar to filters on website. There will be a clear/show selected button to filter list (not required to show on design) - at bottom "Next Choose Winner" button.
We need footer with menu links "Pick Players", "My Beacon", My Games", "My Profile".
If you have any specific questions, please let me know before starting on it.
Updates
This is not a contest for everyone looking to work on it. If you submit your portfolio and ideas, we will work with them directly on the design/delivery. This is my first time posting a project and didn't realize I created a contest.
Target Market(s)
iOS and Android
Look and feel
Each slider illustrates characteristics of the customer's brand and the style your logo design should communicate.

```html
<!DOCTYPE html>
<html lang="en">
<head>
<meta charset="utf-8">
<title>Teebeacon – Pick Players</title>
<link href="https://fonts.googleapis.com/css2?family=Arimo:wght@400;700&family=Bree+Serif&family=Marcellus+SC&display=swap" rel="stylesheet">
<style>
  :root {
    --navy: #1b2f5c;
    --navy-deep: #0d1a36;
    --navy-cell: #2a3a58;
    --red: #d4262a;
    --red-dark: #a81a1d;
    --field: #e9e9e9;
    --row-light: #d4dbea;
    --row-mid: #aeb9d1;
    --arrow-col: #8494b8;
    --ink: #1d2840;
    --gold: #d9ad3c;
    --white: #ffffff;
    --footer: #b6bcc6;
  }
  * { box-sizing: border-box; margin: 0; padding: 0; }
  html, body { width: 1200px; height: 899px; overflow: hidden; background: var(--white); }
  body { position: relative; font-family: "Arimo", Arial, sans-serif; }

  .screen {
    position: absolute; left: 361px; top: 61px; width: 447px; height: 789px;
    background: var(--field); overflow: hidden;
    box-shadow: 0 4px 12px rgba(0,0,0,.35);
  }

  .status-bar {
    height: 24px; background: linear-gradient(#f4f4f4, #d8d8d8);
    display: flex; align-items: center; padding: 0 16px; font-size: 14px; color: #222;
  }
  .status-bar .carrier { display: flex; align-items: center; gap: 4px; width: 150px; }
  .status-bar .time { font-size: 16px; }

  .app-header {
    height: 59px; background: linear-gradient(#24407a, var(--navy-deep));
    display: flex; align-items: center; padding-left: 12px; color: var(--white);
  }
  .brand { font-size: 28px; letter-spacing: -0.5px; flex: 1; }
  .messages { position: relative; margin-right: 20px; }
  .messages .badge {
    position: absolute; right: -6px; top: -8px; width: 14px; height: 14px; border-radius: 50%;
    background: var(--red); border: 1px solid #fff; font-size: 9px; text-align: center; line-height: 12px;
  }
  .points { font-size: 15px; margin-right: 14px; }
  .menu-btn {
    width: 46px; height: 59px; background: var(--navy-deep);
    display: flex; align-items: center; justify-content: center;
  }

  .tournament-bar {
    height: 33px; background: linear-gradient(#e0332f, var(--red-dark));
    display: flex; align-items: center; justify-content: space-between; padding: 0 12px;
    color: var(--white); font-family: "Marcellus SC", serif; font-size: 17px; letter-spacing: 1px;
  }
  .tokens-bar {
    margin-top: 2px; height: 42px; background: linear-gradient(#d7d7d7, #bdbdbd);
    display: flex; align-items: center; padding-left: 16px;
    font-size: 17px; color: #555; letter-spacing: 1px;
  }

  .player-list { position: absolute; left: 2px; top: 213px; width: 420px; height: 459px; overflow: hidden; }
  .list-head { height: 70px; display: flex; background: var(--navy-deep); gap: 2px; }
  .list-head > div { display: flex; align-items: center; justify-content: center; color: #cfd5e0; font-weight: 700; }
  .head-rank { width: 60px; font-size: 26px; }
  .head-avatar { width: 68px; background: linear-gradient(#e4e4e4, #b9b9b9); }
  .head-name { width: 166px; background: linear-gradient(#3a4a68, var(--navy-cell)); font-size: 25px; color: #b9c0cc !important; }
  .head-tokens { width: 50px; background: var(--navy-cell); font-size: 26px; }
  .head-play { flex: 1; background: var(--navy-cell); }

  .player-row { height: 68px; margin-top: 2px; display: flex; background: var(--navy-deep); }
  .player-info {
    width: 298px; position: relative; padding: 6px 0 0 64px;
    background: linear-gradient(var(--row-light), var(--row-mid));
  }
  .player-photo { position: absolute; left: 14px; top: 6px; width: 40px; height: 54px; background: linear-gradient(#8a9a7a, #c9a98e); }
  .token-coin {
    position: absolute; left: 6px; top: 40px; width: 21px; height: 21px; border-radius: 50%;
    background: radial-gradient(#f2d27a, var(--gold)); font-size: 10px; font-weight: 700;
    text-align: center; line-height: 21px; color: #5a4210;
  }
  .player-name { font-family: "Bree Serif", serif; font-size: 18px; color: var(--ink); display: flex; align-items: center; gap: 10px; height: 30px; }
  .player-meta { font-size: 10px; color: #3a4660; margin-top: 4px; }
  .player-meta .stats { text-decoration: underline; margin-left: 6px; }
  .flag { display: inline-block; width: 30px; height: 18px; }
  .flag-us { background: linear-gradient(#3b4a9a,#3b4a9a) 0 0/13px 9px no-repeat, repeating-linear-gradient(#c9252c 0 2px, #fff 2px 4px); }
  .flag-se { background: linear-gradient(#f2c716,#f2c716) 9px 0/4px 100% no-repeat, linear-gradient(#f2c716,#f2c716) 0 7px/100% 4px no-repeat, #1d5ea8; }
  .flag-zw { background: linear-gradient(#2a8a3a 0 20%, #f2c716 20% 40%, #d12a2a 40% 60%, #f2c716 60% 80%, #2a8a3a 80%); }
  .arrow-cell { width: 50px; background: linear-gradient(#9aa8c6, var(--arrow-col)); display: flex; align-items: center; justify-content: center; }
  .check-cell { flex: 1; display: flex; align-items: center; justify-content: center; }

  .scrollbar { position: absolute; left: 427px; top: 213px; width: 9px; height: 382px; border-radius: 5px; background: #c74848; }

  .next-btn {
    position: absolute; left: 84px; top: 681px; width: 275px; height: 46px; border-radius: 5px;
    background: linear-gradient(#e8362f, var(--red-dark)); box-shadow: 0 3px 4px rgba(0,0,0,.4);
    color: var(--white); font-family: "Marcellus SC", serif; font-size: 19px; letter-spacing: 1px;
    display: flex; align-items: center; justify-content: center;
  }
  .app-footer { position: absolute; left: 0; bottom: 0; width: 100%; height: 52px; background: linear-gradient(#d3d7de, var(--footer)); border-top: 1px solid #aab; }
</style>
</head>
<body>
<main class="screen">
  <div class="status-bar">
    <span class="carrier">
      <svg width="16" height="12"><rect x="0" y="7" width="3" height="5" fill="#2a6fd0"/><rect x="4" y="4" width="3" height="8" fill="#2a6fd0"/><rect x="8" y="1" width="3" height="11" fill="#2a6fd0"/></svg>
      NorthCell
      <svg width="22" height="14" viewBox="0 0 22 14" style="margin-left:12px"><path d="M2 5a13 13 0 0 1 18 0M5 8a8.5 8.5 0 0 1 12 0M8 11a4 4 0 0 1 6 0" stroke="#2a6fd0" stroke-width="2" fill="none"/></svg>
    </span>
    <span class="time">12:34 PM</span>
  </div>

  <header class="app-header">
    <span class="brand">Teebeacon</span>
    <span class="messages">
      <svg width="34" height="22" viewBox="0 0 34 22"><rect x="1" y="1" width="32" height="20" fill="#fff"/><path d="M1 1l16 12 16-12" stroke="#777" fill="none"/></svg>
      <span class="badge">1</span>
    </span>
    <span class="points">3420</span>
    <span class="menu-btn">
      <svg width="28" height="26" viewBox="0 0 28 26" fill="#fff"><rect x="0" y="1" width="4" height="3"/><rect x="6" y="1" width="22" height="3"/><rect x="0" y="8" width="4" height="3"/><rect x="6" y="8" width="22" height="3"/><rect x="0" y="15" width="4" height="3"/><rect x="6" y="15" width="22" height="3"/><rect x="0" y="22" width="4" height="3"/><rect x="6" y="22" width="22" height="3"/></svg>
    </span>
  </header>

  <div class="tournament-bar">
    <span>Tournament Info</span>
    <svg width="20" height="14" viewBox="0 0 20 14"><path d="M2 2l8 9 8-9" stroke="#fff" stroke-width="3.5" fill="none"/></svg>
  </div>
  <div class="tokens-bar">TOKENS</div>

  <section class="player-list">
    <div class="list-head">
      <div class="head-rank">#3</div>
      <div class="head-avatar" role="img" aria-label="Player avatar placeholder"></div>
      <div class="head-name">Name</div>
      <div class="head-tokens">20</div>
      <div class="head-play">
        <svg width="42" height="42" viewBox="0 0 42 42"><circle cx="21" cy="21" r="19" fill="#c4cad4" stroke="#0d1a36" stroke-width="2"/><path d="M16 11l14 10-14 10z" fill="#2a3a58"/></svg>
      </div>
    </div>

    <div class="player-row">
      <div class="player-info">
        <div class="player-photo" role="img" aria-label="Player photo"></div>
        <span class="token-coin">20</span>
        <div class="player-name">Carl Whitmore <span class="flag flag-us"></span></div>
        <div class="player-meta">WORLD RANKING: 18 <span class="stats">PLAYER STATISTICS</span></div>
      </div>
      <div class="arrow-cell"><svg width="22" height="26"><path d="M2 1l19 12L2 25z" fill="#5c6f9c"/></svg></div>
      <div class="check-cell"><svg width="42" height="42" viewBox="0 0 42 42"><rect x="3" y="8" width="32" height="32" fill="none" stroke="#fff" stroke-width="3"/><path d="M10 22l8 9 20-28" stroke="#fff" stroke-width="4" fill="none"/></svg></div>
    </div>

    <div class="player-row">
      <div class="player-info">
        <div class="player-photo" role="img" aria-label="Player photo"></div>
        <span class="token-coin">20</span>
        <div class="player-name">Erik Sandvall <span class="flag flag-se"></span></div>
        <div class="player-meta">WORLD RANKING: 27 <span class="stats">PLAYER STATISTICS</span></div>
      </div>
      <div class="arrow-cell"><svg width="22" height="26"><path d="M2 1l19 12L2 25z" fill="#5c6f9c"/></svg></div>
      <div class="check-cell"><svg width="42" height="42" viewBox="0 0 42 42"><rect x="3" y="8" width="32" height="32" fill="none" stroke="#fff" stroke-width="3"/><path d="M10 22l8 9 20-28" stroke="#fff" stroke-width="4" fill="none"/></svg></div>
    </div>

    <div class="player-row">
      <div class="player-info">
        <div class="player-photo" role="img" aria-label="Player photo"></div>
        <span class="token-coin">20</span>
        <div class="player-name">Dale Prescott <span class="flag flag-us"></span></div>
        <div class="player-meta">WORLD RANKING: 33 <span class="stats">PLAYER STATISTICS</span></div>
      </div>
      <div class="arrow-cell"><svg width="22" height="26"><path d="M2 1l19 12L2 25z" fill="#5c6f9c"/></svg></div>
      <div class="check-cell"><svg width="42" height="42" viewBox="0 0 42 42"><rect x="3" y="8" width="32" height="32" fill="none" stroke="#fff" stroke-width="3"/><path d="M10 22l8 9 20-28" stroke="#fff" stroke-width="4" fill="none"/></svg></div>
    </div>

    <div class="player-row">
      <div class="player-info">
        <div class="player-photo" role="img" aria-label="Player photo"></div>
        <span class="token-coin">20</span>
        <div class="player-name">Owen Fairbank <span class="flag flag-us"></span></div>
        <div class="player-meta">WORLD RANKING: 41 <span class="stats">PLAYER STATISTICS</span></div>
      </div>
      <div class="arrow-cell"><svg width="22" height="26"><path d="M2 1l19 12L2 25z" fill="#5c6f9c"/></svg></div>
      <div class="check-cell"><svg width="42" height="42" viewBox="0 0 42 42"><rect x="3" y="8" width="32" height="32" fill="none" stroke="#fff" stroke-width="3"/><path d="M10 22l8 9 20-28" stroke="#fff" stroke-width="4" fill="none"/></svg></div>
    </div>

    <div class="player-row">
      <div class="player-info">
        <div class="player-photo" role="img" aria-label="Player photo"></div>
        <span class="token-coin">20</span>
        <div class="player-name">Tendai Moyo <span class="flag flag-zw"></span></div>
        <div class="player-meta">WORLD RANKING: 56 <span class="stats">PLAYER STATISTICS</span></div>
      </div>
      <div class="arrow-cell"><svg width="22" height="26"><path d="M2 1l19 12L2 25z" fill="#5c6f9c"/></svg></div>
      <div class="check-cell"><svg width="42" height="42" viewBox="0 0 42 42"><rect x="3" y="8" width="32" height="32" fill="none" stroke="#fff" stroke-width="3"/><path d="M10 22l8 9 20-28" stroke="#fff" stroke-width="4" fill="none"/></svg></div>
    </div>

    <div class="player-row">
      <div class="player-info">
        <div class="player-photo" role="img" aria-label="Player photo"></div>
        <span class="token-coin">20</span>
        <div class="player-name">Hugh Ramsey <span class="flag flag-us"></span></div>
        <div class="player-meta">WORLD RANKING: 63 <span class="stats">PLAYER STATISTICS</span></div>
      </div>
      <div class="arrow-cell"><svg width="22" height="26"><path d="M2 1l19 12L2 25z" fill="#5c6f9c"/></svg></div>
      <div class="check-cell"><svg width="42" height="42" viewBox="0 0 42 42"><rect x="3" y="8" width="32" height="32" fill="none" stroke="#fff" stroke-width="3"/><path d="M10 22l8 9 20-28" stroke="#fff" stroke-width="4" fill="none"/></svg></div>
    </div>
  </section>

  <div class="scrollbar"></div>

  <div class="next-btn">Next Choose Winner</div>
  <footer class="app-footer"></footer>
</main>
</body>
</html>
```